Business Card Design

Hoping for a black background business card, minimalistic design.
With the Marble Crest logo you created in white.

I would like to include:
My Name and title
Address (street address)
Reception: (phone number)
Fax: (fax number)
Reception: (email address)
Direct email: (email address)
Instagram: (ig handle)

```html
<!DOCTYPE html>
<html lang="en">
<head>
<meta charset="utf-8">
<title>Marble Crest – Business Card</title>
<link rel="stylesheet" href="https://fonts.googleapis.com/css2?family=Open+Sans:wght@400;700&family=Poppins:wght@400;500&display=swap">
<style>
  :root {
    --page: #dedede;
    --card-dark: #000000;
    --card-light: #ffffff;
    --accent: #e8232a;
    --ink: #111111;
    --logo: #ffffff;
  }
  * { margin: 0; padding: 0; box-sizing: border-box; }
  html, body { width: 1029px; height: 1200px; overflow: hidden; }
  body { background: var(--page); position: relative; font-family: "Poppins", sans-serif; }

  .card {
    position: absolute; left: 176px; width: 677px; height: 386px;
    border-radius: 22px; overflow: hidden; background: var(--card-dark);
    box-shadow: 0 3px 8px rgba(0,0,0,.35);
  }
  .card--front { top: 161px; }
  .card--back { top: 680px; }

  .brand { position: absolute; display: flex; align-items: center; color: var(--logo); }
  .brand__circle { border: 4px solid var(--logo); border-radius: 50%; flex: none; }
  .brand__name { font-family: "Poppins", sans-serif; font-weight: 500; letter-spacing: .09em; white-space: nowrap; }

  .card--front .brand { left: 157px; top: 152px; gap: 24px; }
  .card--front .brand__circle { width: 84px; height: 84px; }
  .card--front .brand__name { font-size: 34px; }

  .card--back .brand { left: 68px; top: 161px; gap: 14px; }
  .card--back .brand__circle { width: 50px; height: 50px; border-width: 3px; }
  .card--back .brand__name { font-size: 19px; }

  .back__rule {
    position: absolute; left: 0; top: 166px; width: 338px; height: 1px;
    background: linear-gradient(90deg, rgba(255,255,255,0), rgba(255,255,255,.18), rgba(255,255,255,0));
  }

  .back__panel { position: absolute; left: 338px; top: 0; right: 0; bottom: 0; background: var(--card-light); }
  .back__accent { position: absolute; left: 333px; width: 5px; background: var(--accent); }
  .back__accent--top { top: 0; height: 82px; }
  .back__accent--bottom { top: 303px; height: 83px; }

  .person { position: absolute; left: 361px; top: 49px; font-family: "Open Sans", sans-serif; color: var(--ink); }
  .person__name { font-size: 26px; font-weight: 400; line-height: 1; letter-spacing: .01em; }
  .person__name strong { font-weight: 700; }
  .person__title { margin-top: 8px; font-size: 13.5px; }

  .contact { position: absolute; left: 362px; top: 0; list-style: none; color: var(--ink); }
  .contact__item { position: absolute; left: 0; display: flex; gap: 10px; width: 300px; }
  .contact__icon {
    width: 25px; height: 23px; border: 2px solid var(--accent); flex: none; margin-top: 1px;
    display: flex; align-items: center; justify-content: center;
  }
  .contact__icon svg { width: 13px; height: 13px; fill: var(--accent); }
  .contact__text { font-size: 15.5px; line-height: 20px; white-space: nowrap; }
  .contact__item--phone { top: 126px; }
  .contact__item--mail { top: 186px; }
  .contact__item--address { top: 246px; }
  .contact__item--social { top: 306px; }
</style>
</head>
<body>

<section class="card card--front">
  <div class="brand">
    <span class="brand__circle"></span>
    <span class="brand__name">MARBLE CREST</span>
  </div>
</section>

<section class="card card--back">
  <div class="back__rule"></div>
  <div class="brand">
    <span class="brand__circle"></span>
    <span class="brand__name">MARBLE CREST</span>
  </div>

  <div class="back__panel"></div>
  <div class="back__accent back__accent--top"></div>
  <div class="back__accent back__accent--bottom"></div>

  <div class="person">
    <h1 class="person__name">JORDAN <strong>HALE</strong></h1>
    <p class="person__title">GRAPHIC DESIGNER</p>
  </div>

  <ul class="contact">
    <li class="contact__item contact__item--phone">
      <span class="contact__icon"><svg viewBox="0 0 24 24"><path d="M6.6 10.8a15.1 15.1 0 0 0 6.6 6.6l2.2-2.2c.3-.3.7-.4 1-.2 1.1.4 2.3.6 3.6.6.6 0 1 .4 1 1V20c0 .6-.4 1-1 1A17 17 0 0 1 3 4c0-.6.4-1 1-1h3.5c.6 0 1 .4 1 1 0 1.3.2 2.5.6 3.6.1.3 0 .7-.2 1z"/></svg></span>
      <span class="contact__text">+01 4470 21856<br>+01 4470 21857</span>
    </li>
    <li class="contact__item contact__item--mail">
      <span class="contact__icon"><svg viewBox="0 0 24 24"><path d="M2 5h20v14H2zm2 2v.5l8 5 8-5V7zm0 2.9V17h16V9.9l-8 5z"/></svg></span>
      <span class="contact__text">hello@marblecrest.com<br>jordan@marblecrest.com</span>
    </li>
    <li class="contact__item contact__item--address">
      <span class="contact__icon"><svg viewBox="0 0 24 24"><path d="M12 3 1.5 12H5v9h5v-6h4v6h5v-9h3.5z"/></svg></span>
      <span class="contact__text">Your City Address<br>Street Location, State, Country</span>
    </li>
    <li class="contact__item contact__item--social">
      <span class="contact__icon"></span>
      <span class="contact__text">marblecrest.studio</span>
    </li>
  </ul>
</section>

</body>
</html>
```